New Company Business Card Design

I have a new company logo and I want a new business card design. I dont know if the logo file i attached is in the correct format or quality. We are a New York City Specialty construction Firm specializing in high risk out of the box projects. I want a simple and classy business card that people will his card is as crisp as the work his company does.

Target Market(s)

Clients in the heavy construction industry in New York City

Industry/Entity Type

Construction Company

Contact Information for Business Card

Simple Classy - DIFFERENT

Font styles to use
Other font styles liked:
• Mach the logo font in some way

Colors

Designer to choose colors to be used in the design.

Requirements
Must have
• Uniqueness
Nice to have
• Nothing particular - Just different and classy - Timeless
Should not have
• Goofy Shit or Gimmicky shit

```html
<!DOCTYPE html>
<html lang="en">
<head>
<meta charset="utf-8">
<title>Halvard Builders – Business Card</title>
<link rel="stylesheet" href="https://fonts.googleapis.com/css2?family=Arimo:wght@400;700&display=swap">
<style>
  :root {
    --backdrop: #2b2b2b;
    --card-white: #f9f9f9;
    --brand-blue: #1479bf;
    --back-blue: #0e82c8;
    --skyline-blue: #0a6aa8;
    --ink: #111111;
    --rule-dark: #151515;
  }
  * { margin: 0; padding: 0; box-sizing: border-box; }
  html, body { width: 1000px; height: 1200px; overflow: hidden; }
  body {
    background: var(--backdrop);
    font-family: "Arimo", Arial, sans-serif;
    position: relative;
  }
  .card {
    position: absolute;
    left: 330px;
    width: 328px;
    height: 548px;
  }
  .card-front { top: 32px; background: var(--card-white); }
  .card-back { top: 618px; background: var(--back-blue); overflow: hidden; }

  .brand-name {
    position: absolute;
    left: 0; right: 0;
    text-align: center;
    font-weight: 700;
    font-size: 26px;
    line-height: 1.15;
    letter-spacing: 1px;
  }
  .card-front .brand-name { top: 70px; color: var(--brand-blue); }
  .card-back .brand-name { top: 222px; color: #ffffff; }

  .front-rule-blue {
    position: absolute; left: 0; right: 0; top: 158px;
    height: 3px; background: var(--brand-blue);
  }
  .front-rule-dark {
    position: absolute; left: 0; right: 0; top: 164px;
    height: 3px; background: var(--rule-dark);
  }

  .holder-name {
    position: absolute; left: 25px; top: 268px;
    font-size: 18px; font-weight: 700; color: var(--brand-blue);
    letter-spacing: 0.3px;
  }
  .contact-list {
    position: absolute; left: 24px; top: 308px;
    list-style: none;
  }
  .contact-item {
    display: flex; align-items: flex-start;
    font-size: 11px; line-height: 12px; color: var(--ink);
  }
  .contact-item svg { width: 14px; height: 14px; flex: none; margin-right: 14px; fill: var(--brand-blue); }
  .contact-item.address { height: 35px; }
  .contact-item.phone { height: 28px; }
  .contact-item.mobile { height: 27px; }
  .contact-item.email { height: 23px; }

  .skyline {
    position: absolute; left: 0; right: 0; bottom: 0; height: 240px;
    background: linear-gradient(to bottom, rgba(10,106,168,0) 0%, var(--skyline-blue) 45%);
  }
</style>
</head>
<body>

  <section class="card card-front">
    <div class="brand-name">HALVARD<br>BUILDERS, INC.</div>
    <div class="front-rule-blue"></div>
    <div class="front-rule-dark"></div>

    <h1 class="holder-name">Marcus T. Ellery</h1>

    <ul class="contact-list">
      <li class="contact-item address">
        <svg viewBox="0 0 14 14"><path d="M7 0a5 5 0 0 0-5 5c0 3.6 5 9 5 9s5-5.4 5-9a5 5 0 0 0-5-5zm0 7a2 2 0 1 1 0-4 2 2 0 0 1 0 4z"/></svg>
        <span>215 Harbor Line Road - Linden,<br>New Jersey 07036</span>
      </li>
      <li class="contact-item phone">
        <svg viewBox="0 0 14 14"><path d="M3 1l2.2 2.6-1.2 1.7c.8 1.8 2.2 3.2 4 4l1.7-1.2L12.3 11l-1.5 1.9C6 12.6 1.4 8 1.1 2.5z"/></svg>
        <span>908-555-0142</span>
      </li>
      <li class="contact-item mobile">
        <svg viewBox="0 0 14 14"><path d="M3.5 0h7v14h-7zM4.8 1.5v8.5h4.4V1.5zM6.2 11.3h1.6v1.4H6.2z"/></svg>
        <span>917-555-0187</span>
      </li>
      <li class="contact-item email">
        <svg viewBox="0 0 14 14"><path d="M0 3h14v8H0zm1.2 1 5.8 4 5.8-4z" fill-rule="evenodd"/></svg>
        <span>marcus@halvard.com</span>
      </li>
      <li class="contact-item web">
        <svg viewBox="0 0 14 14"><circle cx="7" cy="7" r="6.2" fill="none" stroke="#1479bf" stroke-width="1.2"/><path d="M1 7h12M7 1v12" stroke="#1479bf" stroke-width="1" fill="none"/><ellipse cx="7" cy="7" rx="2.8" ry="6.2" fill="none" stroke="#1479bf" stroke-width="1"/></svg>
        <span>www.halvard.com</span>
      </li>
    </ul>
  </section>

  <section class="card card-back">
    <div class="brand-name">HALVARD<br>BUILDERS, INC.</div>
    <div class="skyline" role="img" aria-label="Faint city skyline silhouette with harbor statue along the bottom of the card"></div>
  </section>

</body>
</html>
```